Redesign of existing Web Design Project

I wish to redsesign the web pages on www.bqrl.com.au

Background of Halvern Oakridge

Halvern Oakridge Construction Services was established in 2004 as a boutique construction company offering construction advice and management services. We assist people in the construction minefield – step by step.

We offer services in: -

• Construction Management
• Project Management
• Building

The essence of our business is ensuring every project we undertake achieves the client’s objectives. Our experience has shown the secrets to a profitable project are -

• Planning
• Attention to detail
• Value add

We take the trouble to understand the client’s needs in person. Our hands-on approach ensures those involved deliver to the required quality standards at the scheduled times.

Our area of works include: -

• Residential single and multistorey developments
• Education facilities
• Suburban commercial building and refurbishment
• Health
• Defence
• Industrial

Objective of Acquisition

We are planning to expand our business activities. We are aiming to increase our turnover and use website as an increased passive selling tool.

Possible company type

This is an ideal opportunity for person who can capture readers attention.

Target Market(s)

see www.bqrl.com.au

Industry/Entity Type

Construction

Requirements
Must have
• Capture peoples attention on readers zones

```html
<!DOCTYPE html>
<html lang="en">
<head>
<meta charset="utf-8">
<title>Halvern Oakridge Construction Services</title>
<link rel="stylesheet" href="https://fonts.googleapis.com/css2?family=Arimo:wght@400;700&family=PT+Sans:wght@400&family=Philosopher:wght@400&display=swap">
<style>
:root{
  --bg:#22282b;
  --bg-dark:#1b2023;
  --header:#1f2528;
  --nav-top:#5a5d5f;
  --nav-bottom:#3a3d3f;
  --nav-active:#7fa19c;
  --text:#e6e8e8;
  --muted:#b9bdbf;
  --orange:#d9731a;
  --teal-light:#a9c3bf;
  --teal-dark:#6f918c;
  --welcome-title:#153a38;
  --welcome-text:#2a3b3a;
  --tile:#151a1d;
  --frame:#121618;
}
*{box-sizing:border-box;margin:0;padding:0}
html,body{width:855px;height:1200px;overflow:hidden;background:var(--bg)}
body{position:relative;font-family:"Arimo",Arial,sans-serif;color:var(--text)}
.abs{position:absolute}

.site-header{left:0;top:0;width:855px;height:93px;background:linear-gradient(#2b3235,var(--header))}
.brand{left:45px;top:38px;display:flex;align-items:center;gap:10px}
.brand-mark{width:34px;height:34px;background:#8d9db8}
.brand-name{font-family:"Arimo",Arial,sans-serif;font-size:22px;color:#dfe4ea;white-space:nowrap}
.search{left:591px;top:46px;display:flex}
.search-field{width:166px;height:24px;background:#15191b;border:1px solid #2c3336}
.search-btn{width:59px;height:24px;background:linear-gradient(#555a5c,#3c4042);font-size:11px;color:#e8e8e8;display:flex;align-items:center;justify-content:center}

.main-nav{left:0;top:93px;width:855px;height:34px;background:linear-gradient(var(--nav-top),var(--nav-bottom));border-top:1px solid #6b6e70}
.main-nav ul{list-style:none;display:flex;position:absolute;left:42px;top:0;height:33px}
.main-nav li{font-size:12.5px;color:#eef0f0;padding:0 10px;line-height:33px}
.main-nav li.active{background:var(--nav-active);width:68px;text-align:center;padding:0}

.hero{left:0;top:127px;width:855px;height:313px;background:linear-gradient(#1d2326,#252c2f);border-bottom:1px solid #333a3d}
.hero-frame{left:64px;top:154px;width:730px;height:243px;background:#2a2f31;box-shadow:0 6px 14px rgba(0,0,0,.6)}
.hero-photo{left:77px;top:166px;width:705px;height:220px;background:linear-gradient(100deg,#9a8a74 0%,#5a6f8c 40%,#7896b8 55%,#b68a5a 75%,#6a5a48 100%)}
.arrow{width:26px;height:34px;background:#3a4144;top:259px}
.arrow-left{left:42px;border-radius:17px 0 0 17px}
.arrow-right{left:790px;border-radius:0 17px 17px 0}
.arrow svg{display:block;margin:9px auto}
.dots{left:394px;top:408px;display:flex;gap:8px}
.dot{width:10px;height:10px;border-radius:50%;background:#4d5457}
.dot.on{background:#7e9ad0}

.service-tile{top:452px;width:234px;height:42px;background:var(--tile);font-family:"Philosopher",Georgia,serif;font-size:16px;color:#eef0ee;display:flex;align-items:center;justify-content:center;box-shadow:0 4px 8px rgba(0,0,0,.5)}

.welcome{left:42px;top:507px;width:774px;height:89px;background:linear-gradient(var(--teal-light),var(--teal-dark));padding:9px 22px}
.welcome h1{font-weight:400;font-size:20px;color:var(--welcome-title)}
.welcome p{font-size:11px;line-height:15px;color:var(--welcome-text);margin-top:8px}

.section-title{font-weight:400;font-size:19px;color:var(--orange)}
.who{left:58px;top:622px;width:440px}
.who ul{list-style:none;margin-top:6px;padding-left:11px}
.who li{font-family:"PT Sans",Arial,sans-serif;font-size:10.5px;line-height:21px;color:#e4e6e6}
.who .tagline{font-family:"PT Sans",Arial,sans-serif;font-size:10.5px;margin-top:18px;color:#e4e6e6}
.divider{left:501px;top:612px;width:3px;height:300px;background:linear-gradient(#2e3538,#1a1f21)}

.testimonials{left:536px;top:628px;width:280px}
.testimonial{display:flex;gap:9px;margin-top:12px;margin-bottom:26px}
.avatar{width:63px;height:58px;background:#111517;padding:4px;flex:none}
.avatar div{width:100%;height:100%;background:linear-gradient(#c4c9cf,#44557a)}
.t-meta{font-size:9px;color:#d0d3d4}
.t-head{font-size:10.5px;font-weight:700;margin-top:4px}
.t-body{font-size:10.5px;line-height:16px;color:var(--muted);margin-top:2px}

.projects-title{left:69px;top:898px}
.project{top:941px;width:220px;height:151px;background:var(--frame);padding:7px 9px}
.project div{width:100%;height:100%}
.p-arrow{top:1003px}

.site-footer{left:0;top:1122px;width:855px;height:78px;background:var(--bg-dark)}
.footer-links{left:57px;top:1146px;font-size:10px;color:#c9cdce}
.copyright{left:57px;top:1168px;font-size:10px;color:#c9cdce}
.social{left:670px;top:1148px;display:flex;gap:7px}
.social span{width:30px;height:30px;border-radius:50%;background:linear-gradient(#5e6467,#393e41)}
</style>
</head>
<body>

<header class="site-header abs"></header>
<div class="brand abs"><span class="brand-mark"></span><span class="brand-name">Halvern Oakridge Construction Services</span></div>
<div class="search abs"><div class="search-field"></div><div class="search-btn">Search</div></div>

<nav class="main-nav abs">
  <ul>
    <li class="active">Home</li><li>About Us</li><li>Building</li><li>Construction Management</li><li>Project Management</li><li>Links</li><li>Free Downloads</li><li>Careers</li><li>Contacts</li>
  </ul>
</nav>

<section class="hero abs"></section>
<div class="hero-frame abs"></div>
<div class="hero-photo abs" role="img" aria-label="Builder in a work shirt and tool belt marking up plans on a workbench"></div>
<div class="arrow arrow-left abs"><svg width="8" height="16"><path d="M7 1 1 8l6 7" stroke="#9aa0a3" stroke-width="2" fill="none"/></svg></div>
<div class="arrow arrow-right abs"><svg width="8" height="16"><path d="M1 1l6 7-6 7" stroke="#9aa0a3" stroke-width="2" fill="none"/></svg></div>
<div class="dots abs"><span class="dot"></span><span class="dot"></span><span class="dot on"></span><span class="dot"></span><span class="dot"></span></div>

<div class="service-tile abs" style="left:49px">Project Management</div>
<div class="service-tile abs" style="left:311px">Construction Management</div>
<div class="service-tile abs" style="left:573px">Building</div>

<section class="welcome abs">
  <h1>Welcome to Halvern Oakridge</h1>
  <p>We are a Sydney based Construction Company who can help with all your construction needs. The Halvern Oakridge process helps define your budget, establishes Return on Investment and reduces potential risk.</p>
</section>

<section class="who abs">
  <h2 class="section-title">Who uses us?</h2>
  <ul>
    <li>Architects – to assist with costing a project, value-engineering and project implementation.</li>
    <li>Owner/Builders – to assist with project management, costings, work flow and final sign offs</li>
    <li>Developers – to assist with costings, tender appraisal and project management</li>
    <li>Strata managers – remediation, fire safety</li>
    <li>Sub-contractors – for pricing assistance</li>
    <li>Lessor and lessees – for fit outs and make good work</li>
    <li>Investors – to define profitability, feasibility and risk</li>
    <li>Finance companies – risk analysis</li>
    <li>Solicitors – advisory services</li>
  </ul>
  <p class="tagline">Construction is a minefield. We'll help you through it!</p>
</section>
<div class="divider abs"></div>

<section class="testimonials abs">
  <h2 class="section-title">Testimonials</h2>
  <article class="testimonial"><div class="avatar"><div role="img" aria-label="Client portrait"></div></div><div><p class="t-meta">00 Oct 2012| 00 comments</p><p class="t-head">Duis nec porttitor lorem</p><p class="t-body">Mauris et nisi urna nonfaucibus magna. Integer lacus ante then ullamcorper ut vulputate..</p></div></article>
  <article class="testimonial"><div class="avatar"><div role="img" aria-label="Client portrait"></div></div><div><p class="t-meta">00 Oct 2012 | 00 comments</p><p class="t-head">Aenean interdum</p><p class="t-body">Vestibulum ante ipsum primis in faucibus orci luctus ultrices ante posuere.</p></div></article>
  <article class="testimonial"><div class="avatar"><div role="img" aria-label="Client portrait"></div></div><div><p class="t-meta">00 Oct 2012 | 00 comments</p><p class="t-head">Integer vitae nisl</p><p class="t-body">Duis volutpat ligula laoreet orci lectus placerat Curabitur lectus malesuada pulvinar.</p></div></article>
</section>

<h2 class="section-title projects-title abs">Our Projects</h2>
<svg class="p-arrow abs" style="left:50px" width="12" height="24"><path d="M10 2 2 12l8 10" stroke="#6c7376" stroke-width="3" fill="none"/></svg>
<div class="project abs" style="left:77px"><div role="img" aria-label="Crane and workers silhouetted against a sunset sky" style="background:linear-gradient(#d9a04a,#f0b040 60%,#3a2a18)"></div></div>
<div class="project abs" style="left:315px"><div role="img" aria-label="Site engineer reviewing plans on a construction site" style="background:linear-gradient(#7a8290,#6a5a48)"></div></div>
<div class="project abs" style="left:552px"><div role="img" aria-label="Tower crane over a concrete building frame under blue sky" style="background:linear-gradient(#2f6fd0,#8fb0d8 55%,#8a7f70)"></div></div>
<svg class="p-arrow abs" style="left:793px" width="12" height="24"><path d="M2 2l8 10-8 10" stroke="#6c7376" stroke-width="3" fill="none"/></svg>

<footer class="site-footer abs"></footer>
<p class="footer-links abs">Home | About Us | Building | Construction Management | Project Management | Links | Free Downloads | Careers | Contacts</p>
<p class="copyright abs">Copyright © 2008 Halvern Oakridge, All Rights Reserved - Webmaster &nbsp;&nbsp;&nbsp;| &nbsp;&nbsp;&nbsp;Privacy policy</p>
<div class="social abs"><span></span><span></span><span></span><span></span></div>

</body>
</html>
```